Web Design Project

We are re-starting this project.

This project is for a totally new look and design of a website for Wozzlent. www.wozzlent-example.com.

Wozzlent is a naming protocol for physical locations and can be used for fixed and mobile people, places and things. Find your friends, or find a business. Because Wozzlent locations point to precise geo-physical (GPS) co-ordinates, navigation to a location becomes totally reliable.
Updates

Please see the modified brief for this project

Target Market(s)

Every person and every business can have multiple !Wozzs (Wozzlent locations), so the website needs to be appealing and fun, but easy to use and functional

Industry/Entity Type

Business

Colors
34a6d7

Requirements
Must have
• Uniqueness!

```html
<!DOCTYPE html>
<html lang="en">
<head>
<meta charset="utf-8">
<title>Wozzlent – Find People, Places and Things</title>
<link rel="stylesheet" href="https://fonts.googleapis.com/css2?family=Questrial&family=Orbitron:wght@500&family=Open+Sans:wght@400;700&display=swap">
<style>
:root{
  --brand:#1e98d8;
  --brand-bright:#2fa2dc;
  --brand-soft:#8dcbeb;
  --nav-bg:#f7f7fc;
  --ink-blue:#2a9ad6;
  --white:#ffffff;
  --dark-text:#2b3440;
  --map-dark:#5a5a5c;
  --map-light:#c9c5bb;
}
*{box-sizing:border-box;margin:0;padding:0}
html,body{width:1200px;height:944px;overflow:hidden;background:var(--white)}
body{position:relative;font-family:"Questrial",sans-serif}
h1,h2{font-weight:400}
.hero-map{position:absolute;left:0;top:0;width:1200px;height:723px;
  background:linear-gradient(160deg,var(--map-dark) 0%,#8d8b86 30%,var(--map-light) 55%,#b3b0a8 80%,var(--map-dark) 100%)}
.main-nav{position:absolute;left:78px;top:0;width:1045px;height:101px;background:var(--nav-bg);display:flex}
.nav-home{width:98px;height:101px;background:var(--brand-bright);display:flex;align-items:center;justify-content:center}
.nav-item{flex:1;display:flex;align-items:center;justify-content:center;font-family:"Open Sans",sans-serif;font-weight:700;font-size:14px;color:var(--brand-bright);border-left:1px solid var(--brand-bright);margin:2px 0}
.nav-item:first-of-type{border-left:none}
.account-links{position:absolute;right:87px;top:117px;display:flex;gap:30px;font-family:"Open Sans",sans-serif;font-size:13px;color:var(--brand-bright)}
.account-links span{display:flex;align-items:center;gap:3px}
.brand-name{position:absolute;left:0;width:1200px;top:160px;text-align:center;font-size:78px;color:var(--brand);letter-spacing:-1px}
.auth-panel{position:absolute;left:351px;top:293px;width:503px;height:130px;background:var(--brand);display:flex}
.auth-btn{flex:1;display:flex;flex-direction:column;align-items:center;justify-content:flex-end;padding-bottom:4px;color:var(--white);font-family:"Orbitron",sans-serif;font-size:15px;letter-spacing:3px}
.auth-btn svg{margin-bottom:22px}
.auth-divider{width:1px;background:var(--white);margin:7px 0}
.search-panel{position:absolute;left:83px;top:476px;width:1039px;height:247px;background:var(--brand)}
.search-title{position:absolute;left:0;top:6px;width:1039px;text-align:center;color:var(--white);font-size:46px;letter-spacing:1px}
.search-labels,.search-fields{position:absolute;left:0;top:0;width:1039px;height:0}
.search-labels span{position:absolute;top:87px;color:var(--white);font-family:"Open Sans",sans-serif;font-size:14px;text-align:center;width:252px}
.search-fields span{position:absolute;top:117px;height:35px;width:252px;background:var(--brand-soft);font-family:"Open Sans",sans-serif;font-size:13px;color:var(--dark-text);padding:9px 6px}
.suggestions{position:absolute;left:0;top:167px;width:827px;font-family:"Open Sans",sans-serif;font-size:12.9px;color:var(--white)}
.suggestions li{list-style:none;height:18.5px;line-height:18.5px;padding-left:12px;white-space:nowrap;overflow:hidden}
.suggestions li.active{background:var(--brand-soft);color:var(--brand-bright)}
.lookup-divider{position:absolute;left:827px;top:170px;width:2px;height:77px;background:var(--white)}
.lookup-btn{position:absolute;left:829px;top:197px;width:210px;text-align:center;color:var(--white);font-family:"Orbitron",sans-serif;font-size:19px;letter-spacing:3px}
.feed-title{position:absolute;left:0;width:1195px;top:731px;text-align:center;color:var(--ink-blue);font-size:23px}
.feed-row{position:absolute;left:80px;width:1013px;height:35px;display:flex}
.feed-text{width:635px;background:var(--brand-soft);color:var(--white);font-family:"Questrial",sans-serif;font-size:13px;padding:8px 0 0 60px;white-space:nowrap}
.feed-action{width:152px;background:var(--brand);color:var(--white);font-family:"Open Sans",sans-serif;font-size:14.5px;display:flex;align-items:center;justify-content:center}
.feed-icon{width:36px;background:var(--brand-soft);display:flex;align-items:center;justify-content:center}
.gap{width:3px}
.feed-scroll{position:absolute;left:1101px;top:843px}
.site-footer{position:absolute;left:0;top:914px;width:1200px;height:30px;background:var(--brand);color:var(--white)}
.site-footer .powered{position:absolute;left:892px;top:10px;font-family:"Open Sans",sans-serif;font-size:10px}
.site-footer .footer-brand{position:absolute;left:962px;top:5px;font-size:17px}
</style>
</head>
<body>
<div class="hero-map" role="img" aria-label="Tilted street map of a harbour city used as hero background"></div>

<nav class="main-nav">
  <div class="nav-home">
    <svg width="24" height="22" viewBox="0 0 24 22"><path d="M12 1 1 11h3v10h6v-6h4v6h6V11h3z" fill="#fff"/></svg>
  </div>
  <span class="nav-item">ABOUT</span>
  <span class="nav-item">HELP</span>
  <span class="nav-item">CONTACT</span>
  <span class="nav-item">PRIVACY</span>
  <span class="nav-item">TERMS</span>
  <span class="nav-item">REFUND</span>
  <span class="nav-item">FAQ</span>
</nav>

<div class="account-links">
  <span><svg width="11" height="13" viewBox="0 0 11 13"><rect x="1" y="6" width="9" height="7" fill="#2fa2dc"/><path d="M3 6V4a2.5 2.5 0 0 1 5 0v2" stroke="#2fa2dc" stroke-width="1.6" fill="none"/></svg>Login</span>
  <span><svg width="13" height="13" viewBox="0 0 13 13"><circle cx="6.5" cy="6.5" r="5.5" stroke="#2fa2dc" stroke-width="1.4" fill="none"/><path d="M6.5 3.5v6M3.5 6.5h6" stroke="#2fa2dc" stroke-width="1.4"/></svg>Sign up</span>
</div>

<div class="brand-name">Wozzlent</div>

<div class="auth-panel">
  <div class="auth-btn">
    <svg width="42" height="66" viewBox="0 0 42 66"><path d="M21 1C10 1 1 10 1 21c0 14 20 44 20 44s20-30 20-44C41 10 32 1 21 1z" fill="#fff"/><rect x="13" y="20" width="16" height="13" rx="2" fill="#1e98d8"/><path d="M16 20v-4a5 5 0 0 1 10 0v4" stroke="#1e98d8" stroke-width="2.5" fill="none"/><circle cx="21" cy="26" r="2" fill="#fff"/></svg>
    LOG IN
  </div>
  <div class="auth-divider"></div>
  <div class="auth-btn">
    <svg width="42" height="66" viewBox="0 0 42 66"><path d="M21 1C10 1 1 10 1 21c0 14 20 44 20 44s20-30 20-44C41 10 32 1 21 1z" fill="#fff"/><circle cx="21" cy="20" r="11" stroke="#1e98d8" stroke-width="3" fill="none"/><path d="M21 14v12M15 20h12" stroke="#1e98d8" stroke-width="3"/></svg>
    SIGN UP
  </div>
</div>

<section class="search-panel">
  <h1 class="search-title">Who Would Like To Find?</h1>
  <div class="search-labels">
    <span style="left:0">Find Something or Someone?</span>
    <span style="left:263px">In These Categories</span>
    <span style="left:525px">With these &nbsp;keywords</span>
    <span style="left:787px;top:89px">Area</span>
  </div>
  <div class="search-fields">
    <span style="left:0">Ex: Jordan</span>
    <span style="left:263px">Ex: Jordan</span>
    <span style="left:525px">Ex: Jordan</span>
    <span style="left:787px">Ex: Jordan</span>
  </div>
  <ul class="suggestions">
    <li>Dummy name categories with these keywords address address, Dummy name categories with these keywords address address</li>
    <li class="active">Dummy name categories with these keywords address address, Dummy name categories with these keywords address address</li>
    <li>Dummy name categories with these keywords address address, Dummy name categories with these keywords address address</li>
    <li>Dummy name categories with these keywords address address, Dummy name categories with these keywords address address</li>
  </ul>
  <div class="lookup-divider"></div>
  <div class="lookup-btn">LOOK UP</div>
</section>

<h2 class="feed-title">What is the WOZZLENT™ Social Positioning Phenomenon ?</h2>

<div class="feed-row" style="top:767px">
  <div class="feed-text">Jordan Updated Their Current Location - jordan-example.com - 5 seconds before</div>
  <div class="feed-action">Show Location</div>
  <div class="feed-icon"><svg width="18" height="26" viewBox="0 0 18 26"><path d="M9 1C4.6 1 1 4.6 1 9c0 6 8 16 8 16s8-10 8-16c0-4.4-3.6-8-8-8z" fill="#1e98d8"/><circle cx="9" cy="9" r="3" fill="#8dcbeb"/></svg></div>
  <div class="gap"></div>
  <div class="feed-action">Get Direction</div>
  <div class="feed-icon"><svg width="22" height="26" viewBox="0 0 22 26"><path d="M3 26V8h10V3l8 7-8 7v-5H7v14z" fill="#1e98d8"/></svg></div>
</div>
<div class="feed-row" style="top:805px">
  <div class="feed-text">Jordan Updated Their Current Location - jordan-example.com - 10 seconds before</div>
  <div class="feed-action">Show Location</div>
  <div class="feed-icon"><svg width="18" height="26" viewBox="0 0 18 26"><path d="M9 1C4.6 1 1 4.6 1 9c0 6 8 16 8 16s8-10 8-16c0-4.4-3.6-8-8-8z" fill="#1e98d8"/><circle cx="9" cy="9" r="3" fill="#8dcbeb"/></svg></div>
  <div class="gap"></div>
  <div class="feed-action">Get Direction</div>
  <div class="feed-icon"><svg width="22" height="26" viewBox="0 0 22 26"><path d="M3 26V8h10V3l8 7-8 7v-5H7v14z" fill="#1e98d8"/></svg></div>
</div>
<div class="feed-row" style="top:843px">
  <div class="feed-text">Jordan Updated Their Current Location - jordan-example.com - 15 seconds before</div>
  <div class="feed-action">Show Location</div>
  <div class="feed-icon"><svg width="18" height="26" viewBox="0 0 18 26"><path d="M9 1C4.6 1 1 4.6 1 9c0 6 8 16 8 16s8-10 8-16c0-4.4-3.6-8-8-8z" fill="#1e98d8"/><circle cx="9" cy="9" r="3" fill="#8dcbeb"/></svg></div>
  <div class="gap"></div>
  <div class="feed-action">Get Direction</div>
  <div class="feed-icon"><svg width="22" height="26" viewBox="0 0 22 26"><path d="M3 26V8h10V3l8 7-8 7v-5H7v14z" fill="#1e98d8"/></svg></div>
</div>

<svg class="feed-scroll" width="14" height="36" viewBox="0 0 14 36" aria-label="Scroll feed">
  <path d="M2 8l5-5 5 5M2 13l5-5 5 5M2 23l5 5 5-5M2 28l5 5 5-5" stroke="#2fa2dc" stroke-width="1.6" fill="none"/>
</svg>

<footer class="site-footer">
  <span class="powered">Powered by</span>
  <span class="footer-brand">Wozzlent</span>
</footer>
</body>
</html>
```